Cleaning/ butler service flyer design

We need a flyer that will be distributed through letter boxes for a small company based in Leamington Spa, called Rodrigo and Teodoro - We offer an in depth cleaning service as a one off, or regular weekly cleaning to suit the client. Rodrigo and Teodoro are experienced in hotel housekeeper services, and know the difference between what looks clean and what really is clean. We would like the designs to include green and blue colours. The flyer should also have a hint of humour but communicate trust and flexibility.

I the flyer to capitalise on the personality of these two Spanish guys doing a cleaning service.
- Logo: Use words – Rodrigo & Teodoro
o In Century Gothic Bold font
o Use a hoover to create the ‘&’ giving it the quirky logo

Rodriego & Teodoro
Cleaning at your service

I like the use of the strap line “ we know the difference between what looks clean and what really is clean”

We will provide a phone number and an email address as contact details which should appear at the bottom of the flyer.

Blue and Green colours to be used

I want the flyer to convey the fact that we don’t take our selves too seriously hence the need for humour (a bit like Ignacio in crooked gables), but the Home Cleaning Service is the main service that is offered so please use images that convey ‘Homey’ feelings.

Target Market(s)

Adults aged 36 - 55, men and women who live alone and work long hours and the last thing they want to do is clean their house on a weekend. Families with kids and or pets

Industry/Entity Type

Cleaning Service

Font styles to use
Other font styles liked:
• Century Gothic

Colors
0355a3
00a88f

Requirements
Must have
• I want to place 3 testimonials to evoke the service

```html
<!DOCTYPE html>
<html lang="en">
<head>
<meta charset="utf-8">
<title>Rodrigo &amp; Teodoro – Cleaning at your service</title>
<link rel="stylesheet" href="https://fonts.googleapis.com/css2?family=Montserrat:ital,wght@0,600;0,700;0,800;1,700&family=Pacifico&family=Arimo:wght@400;700&family=Roboto+Condensed:wght@400&display=swap">
<style>
  :root {
    --brand-blue: #0355a3;
    --brand-blue-light: #2a7fd0;
    --brand-green: #00a88f;
    --paper: #ffffff;
    --ink-light: #ffffff;
    --illustration-warm: #e9d6c4;
    --illustration-cool: #a9dad2;
  }
  * { box-sizing: border-box; margin: 0; padding: 0; }
  html, body { width: 929px; height: 1200px; overflow: hidden; background: var(--paper); }
  .flyer {
    position: relative;
    width: 929px;
    height: 1200px;
    background: var(--paper);
    font-family: "Montserrat", "Century Gothic", sans-serif;
    overflow: hidden;
  }

  .strapline {
    position: absolute;
    left: 20px; top: 40px;
    width: 590px;
    text-align: center;
    font-weight: 800;
    font-size: 34px;
    line-height: 48px;
    color: var(--brand-blue);
  }
  .strapline .emphasis {
    display: block;
    color: var(--brand-green);
    font-style: italic;
    font-weight: 700;
    font-size: 40px;
  }

  .brand {
    position: absolute;
    left: 610px; top: 40px;
    width: 300px;
    text-align: center;
  }
  .brand-mark {
    display: flex;
    align-items: center;
    justify-content: center;
    gap: 12px;
    height: 210px;
  }
  .brand-dot {
    width: 26px; height: 26px;
    border-radius: 50%;
    background: var(--brand-green);
    flex: none;
  }
  .brand-name {
    font-weight: 700;
    font-size: 40px;
    line-height: 50px;
    color: var(--brand-blue);
  }
  .brand-tagline {
    margin-top: 26px;
    font-family: "Pacifico", cursive;
    font-size: 28px;
    color: var(--brand-green);
    white-space: nowrap;
  }

  .testimonial {
    position: absolute;
    background: var(--brand-green);
    color: var(--ink-light);
    font-family: "Roboto Condensed", "Arial Narrow", sans-serif;
    font-size: 16px;
    line-height: 20px;
    text-align: center;
    border-radius: 40px;
    padding: 16px 22px;
  }
  .testimonial::after {
    content: "";
    position: absolute;
    width: 0; height: 0;
    border-style: solid;
    bottom: -20px;
  }
  .testimonial--first { left: 54px; top: 362px; width: 342px; }
  .testimonial--first::after { right: 46px; border-width: 22px 0 0 26px; border-color: var(--brand-green) transparent transparent transparent; }
  .testimonial--second { left: 462px; top: 516px; width: 214px; padding: 16px 18px; }
  .testimonial--second::after { left: 36px; border-width: 22px 26px 0 0; border-color: var(--brand-green) transparent transparent transparent; }
  .testimonial--third { left: 24px; top: 590px; width: 372px; }
  .testimonial--third::after { right: 50px; border-width: 22px 0 0 26px; border-color: var(--brand-green) transparent transparent transparent; }

  .illustration {
    position: absolute;
    left: 690px; top: 372px;
    width: 214px; height: 330px;
    border-radius: 30px;
    background: linear-gradient(160deg, var(--illustration-warm) 0%, var(--illustration-cool) 100%);
  }

  .speech-bubble {
    position: absolute;
    left: 648px; top: 682px;
    width: 152px; height: 92px;
    border: 3px solid var(--brand-blue);
    border-radius: 50%;
    background: var(--paper);
    display: flex; align-items: center; justify-content: center;
    text-align: center;
    font-family: "Arimo", Arial, sans-serif;
    font-weight: 700;
    font-size: 19px;
    line-height: 22px;
    color: var(--brand-blue);
  }

  .experience {
    position: absolute;
    left: 420px; top: 796px;
    width: 490px;
    text-align: center;
    font-weight: 700;
    font-size: 24px;
    line-height: 31px;
    color: var(--brand-blue);
  }

  .call-to-action {
    position: absolute;
    left: 0; top: 952px;
    width: 929px;
    text-align: center;
    font-weight: 700;
    font-style: italic;
    font-size: 33px;
    color: var(--brand-green);
  }

  .contact {
    position: absolute;
    left: 0; top: 1042px;
    width: 929px;
    display: flex;
    justify-content: center;
    gap: 44px;
    font-family: "Arimo", Arial, sans-serif;
    font-weight: 700;
    font-size: 26px;
    color: var(--brand-blue);
  }
  .contact-item { display: flex; align-items: center; gap: 10px; }
  .contact-icon { width: 28px; height: 28px; flex: none; }

  .services {
    position: absolute;
    left: 0; top: 1094px;
    width: 929px; height: 106px;
    background: linear-gradient(90deg, var(--brand-blue) 0%, var(--brand-blue-light) 100%);
    padding: 6px 0 0 124px;
    list-style: none;
    font-family: "Arimo", Arial, sans-serif;
    font-size: 22px;
    line-height: 24px;
    color: var(--ink-light);
  }
  .services li { width: 560px; }
</style>
</head>
<body>
<main class="flyer">

  <h1 class="strapline">
    We know the<br>
    difference between
    <span class="emphasis">what looks clean</span>
    and
    <span class="emphasis">what really is clean...</span>
  </h1>

  <header class="brand">
    <div class="brand-mark">
      <span class="brand-dot"></span>
      <span class="brand-name">RODRIGO<br>&amp;<br>TEODORO</span>
    </div>
    <p class="brand-tagline">Cleaning at your service</p>
  </header>

  <blockquote class="testimonial testimonial--first">
    “We really struggled to find a reliable cleaning service that was consistent week in week out, these two Spanish guys turned up and have done and continue to do a really good job – Olé!” Harriet – Linden Avenue
  </blockquote>

  <blockquote class="testimonial testimonial--second">
    “They even texted me after to ask if I was happy with the service” Gareth – Elm Gates
  </blockquote>

  <blockquote class="testimonial testimonial--third">
    “I suffer from dust allergies, so I can tell when a cleaner hasn’t been through. I’ve been through loads and I can tell you, these guys really do clean” Rupert – Ashcombe
  </blockquote>

  <div class="illustration" role="img" aria-label="Cartoon of a child with arms folded sitting on an upturned cleaning bucket"></div>

  <p class="speech-bubble">“But mom!<br>It’s CLEAN!”</p>

  <p class="experience">
    RODRIGO AND TEODORO<br>
    ARE EXPERIENCED<br>
    IN HOTEL HOUSEKEEPER SERVICES
  </p>

  <p class="call-to-action">Call today for our in depth cleaning service!</p>

  <div class="contact">
    <span class="contact-item">
      <svg class="contact-icon" viewBox="0 0 28 28" aria-hidden="true">
        <rect x="2" y="6" width="24" height="16" fill="none" stroke="#0355a3" stroke-width="2.5"/>
        <path d="M2 6 L14 16 L26 6" fill="none" stroke="#0355a3" stroke-width="2.5"/>
      </svg>
      hello@rtclean.example
    </span>
    <span class="contact-item">
      <svg class="contact-icon" viewBox="0 0 28 28" aria-hidden="true">
        <path d="M7 3 L11 3 L13 9 L10 11 C11.5 14.5 13.5 16.5 17 18 L19 15 L25 17 L25 21 C25 23 23 25 21 25 C11 24 4 17 3 7 C3 5 5 3 7 3 Z" fill="#0355a3"/>
      </svg>
      555.555.0142
    </span>
  </div>

  <ul class="services">
    <li>In-depth cleaning</li>
    <li>Dog walking service available</li>
    <li>Additional services to assist in the smooth running<br>of the household</li>
  </ul>

</main>
</body>
</html>
```